Halvern Dental website redesign

We need a redesign for a website: myhalverndental.com.

I already created a video going over what exactly is needed in the design.

See Video here: https://files.quorvane.com/file/d/8xKpQ2mWn4TzLrV7bHsYcE3jFuGaD6oN1/view?usp=sharing

Reviewly Slide shown in Video: https://slides.quorvane.com/presentation/d/7RtW2yQnXbVc4LmPz9KsHdJf3GaE8oUi6TeYqNvB5wZx/edit?usp=sharing
Updates

Holidays in India so we did not get enough design entries or quality.

Target Market(s)

Dentistry

Industry/Entity Type

Dentistry

Number of Pages Required

1 page

Colors
0094D4
00A9DD
6FCCEA
C7EBF8
E9F6FB
00AB8E
00BBA5
67D7C9
C6EFE9
E9F9F6

Requirements
Must have
• See 13 min video link in description - shows what to do.

```html
<!DOCTYPE html>
<html lang="en">
<head>
<meta charset="utf-8">
<title>Halvern Dental</title>
<link rel="stylesheet" href="https://fonts.googleapis.com/css2?family=Poppins:wght@400;500;600;700&family=Lora:wght@400;500;600&family=Open+Sans:wght@400;600&display=swap">
<style>
:root{
  --navy:#0f2b40;
  --navy-deep:#0a2030;
  --blue:#0094D4;
  --blue-2:#00A9DD;
  --blue-3:#6FCCEA;
  --blue-4:#C7EBF8;
  --blue-5:#E9F6FB;
  --green:#3fae49;
  --teal:#00AB8E;
  --teal-2:#00BBA5;
  --teal-3:#67D7C9;
  --ink:#2c3a44;
  --muted:#6b7780;
  --star:#f5b400;
  --white:#ffffff;
}
*{box-sizing:border-box;margin:0;padding:0}
html,body{width:1200px;height:4460px;overflow:hidden}
body{font-family:"Open Sans",Arial,sans-serif;color:var(--ink);background:var(--white);position:relative}
.abs{position:absolute}
.serif-heading{font-family:"Lora",Georgia,serif;font-weight:500;color:var(--green);text-align:center}
.btn{display:inline-block;font-family:"Poppins",Arial,sans-serif;font-weight:500;font-size:14px;color:#fff;background:var(--blue);padding:11px 26px;border-radius:4px}
.btn-green{background:var(--green)}
.lead{font-size:12.5px;line-height:20px;color:var(--muted);text-align:center}

/* header */
.site-header{left:0;top:0;width:1200px;height:64px;background:var(--navy)}
.top-tabs{right:20px;top:0;display:flex;gap:4px}
.top-tabs span{font-family:"Poppins",sans-serif;font-size:12px;color:#fff;padding:6px 16px;border-radius:0 0 4px 4px}
.tab-schedule{background:var(--green)}
.tab-emergency{background:var(--blue)}
.brand{left:28px;top:18px;display:flex;align-items:center;gap:8px}
.brand-dot{width:14px;height:14px;border-radius:50%;background:var(--green)}
.brand-name{font-family:"Poppins",sans-serif;font-weight:600;font-size:20px;color:#fff}
.main-nav{left:300px;top:38px;display:flex;gap:18px;font-family:"Poppins",sans-serif;font-size:12px;color:#dbe6ee}
.main-nav .active{background:var(--green);color:#fff;padding:2px 10px;margin-top:-2px;border-radius:3px}
.header-call{left:1040px;top:32px;display:flex;align-items:center;gap:8px;color:#fff;font-family:"Poppins",sans-serif}
.header-call small{display:block;font-size:10px;line-height:12px;color:#b8c8d4}
.header-call b{font-size:14px;font-weight:600;line-height:18px}

/* hero */
.hero-photo{left:0;top:64px;width:1200px;height:700px;background:linear-gradient(120deg,#e9e2dc 0%,#f3ece6 35%,#d7e6ef 70%,#bcd7e6 100%)}
.hero-badge{left:660px;top:190px;width:430px;height:430px;border-radius:50%;border:14px solid var(--green);background:radial-gradient(circle at 40% 35%,#1c4a66,var(--navy) 70%);display:flex;flex-direction:column;align-items:center;justify-content:center;text-align:center;color:#fff}
.hero-badge h1{font-family:"Poppins",sans-serif;font-weight:700;font-size:38px;line-height:44px}
.hero-badge p{font-size:13px;color:var(--teal-3);margin:8px 0 20px}
.hero-wave{left:0;top:640px}

/* team */
.team{left:0;top:780px;width:1200px}
.team h2{font-size:30px}
.team .lead{width:560px;margin:12px auto 0}
.team-grid{display:flex;justify-content:center;gap:100px;margin-top:36px}
.doctor{width:170px;text-align:center}
.doctor-photo{width:170px;height:180px;border-radius:4px;background:linear-gradient(180deg,#dfe6ea,#b7c6cf)}
.doctor h3{font-family:"Lora",serif;font-weight:500;font-size:15px;color:var(--blue);margin-top:12px}
.doctor p{font-size:11px;color:var(--muted);margin-top:2px}

/* services */
.services-bg{left:0;top:1340px}
.services-head{left:0;top:1400px;width:1200px}
.services-head h2{font-size:30px}
.services-head .lead{width:420px;margin:10px auto 0}
.service-list{left:100px;top:1540px;display:grid;grid-template-columns:230px 230px;column-gap:24px;row-gap:14px}
.service{height:40px;background:#fff;border:1px solid var(--blue-4);border-radius:5px;display:flex;align-items:center;gap:10px;padding:0 10px;font-size:12.5px;color:var(--ink);box-shadow:0 2px 5px rgba(0,148,212,.08)}
.service.active{border-color:var(--green)}
.service i{width:22px;height:22px;border-radius:4px;background:var(--blue-5);border:1px solid var(--blue-3)}
.service-photo{left:740px;top:1510px;width:360px;height:360px;border-radius:50%;border:12px solid var(--green);background:linear-gradient(140deg,#eadfd6,#cfe4ef 70%,#9ccde6)}

/* testimonials */
.reviews{left:0;top:1960px;width:1200px;text-align:center}
.reviews h2{font-size:30px}
.rating-label{font-size:12px;color:var(--muted);margin-top:10px}
.rating{display:flex;justify-content:center;align-items:center;gap:10px;margin-top:6px;font-family:"Poppins",sans-serif;font-weight:600;font-size:18px}
.stars{color:var(--star);letter-spacing:4px;font-size:22px}
.review-count{display:inline-flex;align-items:center;gap:8px;margin-top:10px;font-size:12px;color:var(--muted)}
.review-count i{width:22px;height:22px;border-radius:50%;background:var(--blue)}
.avatars{display:flex;justify-content:center;align-items:center;gap:28px;margin-top:22px}
.avatar{width:74px;height:74px;border-radius:50%;background:linear-gradient(180deg,#d8d8d8,#8f9aa2)}
.avatar.big{width:100px;height:100px;border:4px solid var(--green)}
.quote{width:600px;margin:24px auto 0;font-size:12.5px;line-height:20px;color:var(--muted)}
.quote-stars{margin-top:16px;font-size:20px}
.reviewer{font-family:"Poppins",sans-serif;font-size:13px;font-weight:500;margin-top:4px}
.review-sites{display:flex;justify-content:center;gap:36px;margin-top:22px;font-family:"Open Sans",sans-serif;font-weight:600;font-size:15px;color:var(--blue)}
.arrow{top:2290px;width:32px;height:32px;border-radius:50%;background:#eef2f4;display:flex;align-items:center;justify-content:center}

/* experience */
.experience-bg{left:0;top:2490px}
.experience-title{left:70px;top:2580px;width:520px;color:#fff;text-align:center}
.experience-title h2{font-family:"Lora",serif;font-weight:500;font-size:34px;line-height:44px}
.experience-photo{left:0;top:2700px;width:560px;height:480px;background:linear-gradient(130deg,#e8eef1,#c7d8e0 60%,#9dbccb);border-radius:0 260px 260px 0}
.experience-copy{left:640px;top:2620px;width:480px;color:#eaf6fb;font-size:12.5px;line-height:20px}
.experience-copy p{margin-bottom:14px}
.experience-copy .note{color:#fff;font-family:"Lora",serif;font-size:16px;text-decoration:underline;margin-top:20px}

/* commitment */
.commit{left:0;top:3360px;width:1200px;text-align:center}
.commit h2{font-size:32px;line-height:42px}
.commit p{font-size:13px;color:var(--muted);margin:8px 0 18px}
.commit-photo{left:320px;top:3560px;width:560px;height:300px;background:linear-gradient(180deg,#eef3f6,#cfe0ea 60%,#a9cbe0)}

/* footer */
.footer-brand{left:0;top:3920px;width:1200px;display:flex;justify-content:center;align-items:center;gap:10px}
.footer-brand .brand-dot{width:18px;height:18px}
.footer-brand span{font-family:"Poppins",sans-serif;font-weight:600;font-size:30px;color:var(--green)}
.site-footer{left:0;top:4070px;width:1200px;height:330px;background:var(--navy);color:#cfdbe4}
.footer-col{top:40px}
.footer-col h4{font-family:"Lora",serif;font-weight:500;font-size:18px;color:var(--green);margin-bottom:18px}
.contact-line{display:flex;gap:10px;align-items:flex-start;font-size:12.5px;line-height:18px;margin-bottom:12px}
.socials{display:flex;gap:10px;margin-top:16px}
.socials i{width:28px;height:28px;border-radius:50%;border:1px solid var(--green)}
.map{width:330px;height:150px;background:linear-gradient(135deg,#e6ebe5,#d5dfe4)}
.map-caption{font-size:11px;line-height:16px;margin-top:10px;color:#aebdc8}
.hours li{list-style:none;display:flex;gap:10px;align-items:center;font-size:12.5px;margin-bottom:10px}
.hours li::before{content:"";width:8px;height:8px;border-radius:50%;background:var(--green)}
.bottom-bar{left:0;top:4400px;width:1200px;height:60px;background:var(--navy-deep);display:flex;align-items:center;justify-content:center;font-size:11.5px;color:#9fb0bc}
</style>
</head>
<body>

<!-- Header -->
<header class="abs site-header">
  <div class="abs brand"><span class="brand-dot"></span><span class="brand-name">Halvern Dental</span></div>
  <nav class="abs main-nav">
    <span class="active">Home</span><span>About Us</span><span>Services</span><span>Financing</span><span>Testimonials</span><span>New Patient Visit</span><span>Specials</span><span>Contact Us</span><span>Blog</span>
  </nav>
  <div class="abs top-tabs"><span class="tab-schedule">Schedule Online</span><span class="tab-emergency">Emergency</span></div>
  <div class="abs header-call">
    <svg width="18" height="18" viewBox="0 0 24 24"><path fill="#3fae49" d="M6.6 10.8a15 15 0 0 0 6.6 6.6l2.2-2.2a1 1 0 0 1 1-.25 11.4 11.4 0 0 0 3.6.6 1 1 0 0 1 1 1V20a1 1 0 0 1-1 1A17 17 0 0 1 3 4a1 1 0 0 1 1-1h3.5a1 1 0 0 1 1 1c0 1.25.2 2.45.6 3.6a1 1 0 0 1-.25 1z"/></svg>
    <div><small>Give us a call</small><b>(555) 214-0380</b></div>
  </div>
</header>

<!-- Hero -->
<div class="abs hero-photo" role="img" aria-label="Photo of a smiling patient during a dental check-up"></div>
<svg class="abs hero-wave" width="1200" height="140" viewBox="0 0 1200 140">
  <path d="M0 70 Q600 150 1200 40 L1200 140 L0 140 Z" fill="#fff"/>
  <path d="M0 70 Q600 150 1200 40" fill="none" stroke="#0094D4" stroke-width="5"/>
  <path d="M0 82 Q600 160 1200 54" fill="none" stroke="#3fae49" stroke-width="5"/>
</svg>
<div class="abs hero-badge">
  <h1>Creating<br>Healthier Smiles</h1>
  <p>With Advanced Technology and Affordable Treatment</p>
  <span class="btn btn-green">Book An Appointment</span>
</div>

<!-- Team -->
<section class="abs team">
  <h2 class="serif-heading">Meet Our Team</h2>
  <p class="lead">Our friendly team gives you the care you deserve at every visit. Our experienced doctors listen closely and guide you toward the right solution for your smile.</p>
  <div class="team-grid">
    <div class="doctor"><div class="doctor-photo" role="img" aria-label="Portrait of Dr. Anika Rao"></div><h3>Meet Dr. Anika Rao</h3><p>Cosmetic Dentist</p></div>
    <div class="doctor"><div class="doctor-photo" role="img" aria-label="Portrait of Dr. Priya Desai"></div><h3>Meet Dr. Priya Desai</h3><p>Orthodontist</p></div>
    <div class="doctor"><div class="doctor-photo" role="img" aria-label="Portrait of Dr. Rohan Mehta"></div><h3>Meet Dr. Rohan Mehta</h3><p>General Dentist</p></div>
  </div>
</section>

<!-- Services -->
<svg class="abs services-bg" width="1200" height="560" viewBox="0 0 1200 560">
  <path d="M0 40 Q600 -30 1200 40 L1200 520 Q600 580 0 520 Z" fill="#E9F6FB"/>
</svg>
<div class="abs services-head">
  <h2 class="serif-heading">Our Services</h2>
  <p class="lead">We treat every patient like family. Our services help you restore health and bring back your confidence.</p>
</div>
<div class="abs service-list">
  <div class="service active"><i></i>Dental Implants</div><div class="service"><i></i>Gum Disease</div>
  <div class="service"><i></i>Cosmetic Dentistry</div><div class="service"><i></i>Root Canal</div>
  <div class="service"><i></i>Braces</div><div class="service"><i></i>Dentures</div>
  <div class="service"><i></i>Crowns</div><div class="service"><i></i>Emergency Dentistry</div>
  <div class="service"><i></i>Bridge</div><div class="service"><i></i>Veneers</div>
  <div class="service"><i></i>Extractions</div><div class="service"><i></i>Invisible Aligners</div>
</div>
<div class="abs service-photo" role="img" aria-label="Photo of a smiling patient in the dental chair"></div>

<!-- Testimonials -->
<section class="abs reviews">
  <h2 class="serif-heading">What Our Patients Say About Us</h2>
  <p class="rating-label">Average Rating</p>
  <div class="rating"><span class="stars">★★★★★</span>4.9</div>
  <div class="review-count"><i></i>336 Reviews</div>
  <div class="avatars">
    <div class="avatar" role="img" aria-label="Patient photo"></div>
    <div class="avatar big" role="img" aria-label="Patient photo"></div>
    <div class="avatar" role="img" aria-label="Patient photo"></div>
  </div>
  <p class="quote">"As one of my first visits to the dentist in years, this office made me feel at ease right away. The staff was kind, efficient and professional. They explained every step, kept the visit on time and made sure I was comfortable. I would recommend this office to anyone looking for caring, honest dentists."</p>
  <div class="stars quote-stars">★★★★★</div>
  <p class="reviewer">Daniel K.</p>
  <div class="review-sites"><span>Reviewly</span><span>Friendbook</span><span>Localstar</span></div>
</section>
<div class="abs arrow" style="left:150px"><svg width="12" height="12" viewBox="0 0 12 12"><path d="M8 1 3 6l5 5" fill="none" stroke="#6b7780" stroke-width="2"/></svg></div>
<div class="abs arrow" style="left:1018px"><svg width="12" height="12" viewBox="0 0 12 12"><path d="M4 1l5 5-5 5" fill="none" stroke="#6b7780" stroke-width="2"/></svg></div>

<!-- Experience -->
<svg class="abs experience-bg" width="1200" height="780" viewBox="0 0 1200 780">
  <defs><linearGradient id="expGrad" x1="0" y1="0" x2="1" y2="1"><stop offset="0" stop-color="#0094D4"/><stop offset="1" stop-color="#00AB8E"/></linearGradient></defs>
  <path d="M0 70 Q600 -20 1200 60 L1200 720 Q600 800 0 740 Z" fill="url(#expGrad)"/>
</svg>
<div class="abs experience-title"><h2>Experience the Halvern Dental Difference</h2></div>
<div class="abs experience-photo" role="img" aria-label="Photo of a dentist showing a patient her X-ray"></div>
<div class="abs experience-copy">
  <p>Your comfort is our priority at Halvern Dental. We provide affordable care and modern dental solutions. Whether you are looking for a family dentist or need emergency care, our team is ready to help. We take time to learn your goals and explain each option so you feel sure about every decision.</p>
  <p>Our office offers gentle cleanings, cosmetic work and restorative care under one roof. We use digital X-rays and current tools so visits are quick, safe and comfortable for patients of every age.</p>
  <p>We accept most PPO plans and offer flexible payment options, so quality care stays within reach. Our front desk will gladly review your benefits before treatment begins.</p>
  <p>We welcome new patients and are proud to serve our neighbors. Call us or book online to schedule a visit, and let our friendly team help you keep a healthy, confident smile for years to come.</p>
  <p class="note">We are available for Emergencies and Walk-ins.</p>
</div>

<!-- Commitment -->
<section class="abs commit">
  <h2 class="serif-heading">Committed to excellence in<br>Oral Health Care</h2>
  <p>Free Exam and X-Rays for New Patients</p>
  <span class="btn btn-green">Book An Appointment</span>
</section>
<div class="abs commit-photo" role="img" aria-label="Photo of a dentist and assistant treating a young girl"></div>

<!-- Footer -->
<div class="abs footer-brand"><span class="brand-dot"></span><span>Halvern Dental</span></div>
<footer class="abs site-footer">
  <div class="abs footer-col" style="left:80px;width:280px">
    <h4>Contact Us</h4>
    <div class="contact-line"><svg width="14" height="16" viewBox="0 0 14 18"><path d="M7 0a7 7 0 0 0-7 7c0 5 7 11 7 11s7-6 7-11a7 7 0 0 0-7-7zm0 9.5A2.5 2.5 0 1 1 7 4.5a2.5 2.5 0 0 1 0 5z" fill="#3fae49"/></svg><span>128 Larkfield Ave, Suite 3<br>Corvane, CA 90000</span></div>
    <div class="contact-line"><svg width="14" height="14" viewBox="0 0 24 24"><path fill="#3fae49" d="M6.6 10.8a15 15 0 0 0 6.6 6.6l2.2-2.2a1 1 0 0 1 1-.25 11.4 11.4 0 0 0 3.6.6 1 1 0 0 1 1 1V20a1 1 0 0 1-1 1A17 17 0 0 1 3 4a1 1 0 0 1 1-1h3.5a1 1 0 0 1 1 1c0 1.25.2 2.45.6 3.6a1 1 0 0 1-.25 1z"/></svg><span>(555) 214-0380</span></div>
    <div class="contact-line"><svg width="14" height="12" viewBox="0 0 16 12"><rect x="0.5" y="0.5" width="15" height="11" fill="none" stroke="#3fae49"/><path d="M.5.5 8 7l7.5-6.5" fill="none" stroke="#3fae49"/></svg><span>hello@myhalverndental.com</span></div>
    <div class="socials"><i></i><i></i><i></i><i></i></div>
  </div>
  <div class="abs footer-col" style="left:440px;width:330px">
    <h4>Location Map</h4>
    <div class="map" role="img" aria-label="Map showing the office location"></div>
    <p class="map-caption">Halvern Dental, 128 Larkfield Ave, Suite 3<br>Corvane, CA 90000 · Get Directions</p>
  </div>
  <div class="abs footer-col" style="left:880px;width:260px">
    <h4>Office Hours</h4>
    <ul class="hours">
      <li>Monday 9AM - 7PM</li><li>Tuesday 9AM - 7PM</li><li>Wednesday 9AM - 7PM</li><li>Thursday 9AM - 7PM</li><li>Friday 9AM - 5PM</li><li>Saturday 9AM - 2PM</li>
    </ul>
  </div>
</footer>
<div class="abs bottom-bar">Halvern Dental © 2024 All Rights Reserved | Accessibility | Terms | Privacy | Sitemap</div>

</body>
</html>
```